photowall advertisement

We require a wall featuring our company logo. We would like to avoid the color green, and gold is highly preferred. The design should be similar to the one in the attached photo. The wall will be used for photos and promotional purposes during congresses. Files must be prepared for printing.
dimension of wall: 470x223 cm

Industry/Entity Type

lifestyle

Colors
0054AA
0677BA
7BADD7
CADEEF
E8F1F8
6B429C
8869AF
B7A5CE
E3DAEB
F3F0F8

Requirements
Must have
• gold color, white, and other compare with gold color
Nice to have
• some pictograms, maps of Europe

```html
<!DOCTYPE html>
<html lang="en">
<head>
<meta charset="utf-8">
<title>Aurel Vanta – Photo Wall</title>
<link rel="stylesheet" href="https://fonts.googleapis.com/css2?family=Michroma&display=swap">
<style>
  :root {
    --gold: #E2C459;
    --white: #FFFFFF;
    --tile-edge: #ECECEC;
    --night: #000000;
    --night-warm: #0B0904;
  }
  * { margin: 0; padding: 0; box-sizing: border-box; }
  html, body {
    width: 1200px;
    height: 569px;
    overflow: hidden;
    background: var(--white);
  }
  .wall {
    position: relative;
    width: 1200px;
    height: 569px;
    background: var(--white);
    font-family: "Michroma", sans-serif;
    color: var(--gold);
  }
  .tile-row {
    position: absolute;
    left: 0;
    width: 1200px;
    display: flex;
    justify-content: center;
    gap: 17.5px;
  }
  .brand-tile {
    width: 150px;
    height: 36px;
    border-radius: 8px;
    background: var(--white);
    box-shadow: 0 0 0 1px var(--tile-edge), 0 1px 3px rgba(0,0,0,0.06);
    display: flex;
    align-items: center;
    justify-content: center;
    gap: 7px;
  }
  .brand-mark {
    width: 12px;
    height: 12px;
    background: var(--gold);
    flex: none;
  }
  .brand-name {
    font-size: 9.5px;
    font-weight: 400;
    letter-spacing: 0.06em;
    white-space: nowrap;
    line-height: 1;
  }
  .feature-row {
    position: absolute;
    top: 170px;
    left: 0;
    width: 1200px;
    height: 56px;
  }
  .feature-brand {
    position: absolute;
    top: 0;
    width: 300px;
    height: 56px;
    display: flex;
    align-items: center;
    justify-content: center;
    gap: 14px;
  }
  .feature-brand .brand-mark { width: 34px; height: 34px; }
  .feature-brand .brand-name { font-size: 22px; letter-spacing: 0.05em; }
  .feature-brand--left { left: 35px; }
  .feature-brand--center { left: 450px; }
  .feature-brand--right { left: 860px; }
  .gold-rule {
    position: absolute;
    top: 490px;
    left: 0;
    width: 1200px;
    height: 3px;
    background: var(--gold);
  }
  .skyline-band {
    position: absolute;
    top: 493px;
    left: 0;
    width: 1200px;
    height: 76px;
    background: linear-gradient(180deg, var(--night) 0%, var(--night-warm) 100%);
  }
</style>
</head>
<body>
<main class="wall">
  <div class="tile-row" style="top:13px">
    <div class="brand-tile"><span class="brand-mark"></span><span class="brand-name">AUREL VANTA</span></div>
    <div class="brand-tile"><span class="brand-mark"></span><span class="brand-name">AUREL VANTA</span></div>
    <div class="brand-tile"><span class="brand-mark"></span><span class="brand-name">AUREL VANTA</span></div>
    <div class="brand-tile"><span class="brand-mark"></span><span class="brand-name">AUREL VANTA</span></div>
    <div class="brand-tile"><span class="brand-mark"></span><span class="brand-name">AUREL VANTA</span></div>
    <div class="brand-tile"><span class="brand-mark"></span><span class="brand-name">AUREL VANTA</span></div>
    <div class="brand-tile"><span class="brand-mark"></span><span class="brand-name">AUREL VANTA</span></div>
  </div>
  <div class="tile-row" style="top:61px">
    <div class="brand-tile"><span class="brand-mark"></span><span class="brand-name">AUREL VANTA</span></div>
    <div class="brand-tile"><span class="brand-mark"></span><span class="brand-name">AUREL VANTA</span></div>
    <div class="brand-tile"><span class="brand-mark"></span><span class="brand-name">AUREL VANTA</span></div>
    <div class="brand-tile"><span class="brand-mark"></span><span class="brand-name">AUREL VANTA</span></div>
    <div class="brand-tile"><span class="brand-mark"></span><span class="brand-name">AUREL VANTA</span></div>
    <div class="brand-tile"><span class="brand-mark"></span><span class="brand-name">AUREL VANTA</span></div>
  </div>
  <div class="tile-row" style="top:108px">
    <div class="brand-tile"><span class="brand-mark"></span><span class="brand-name">AUREL VANTA</span></div>
    <div class="brand-tile"><span class="brand-mark"></span><span class="brand-name">AUREL VANTA</span></div>
    <div class="brand-tile"><span class="brand-mark"></span><span class="brand-name">AUREL VANTA</span></div>
    <div class="brand-tile"><span class="brand-mark"></span><span class="brand-name">AUREL VANTA</span></div>
    <div class="brand-tile"><span class="brand-mark"></span><span class="brand-name">AUREL VANTA</span></div>
    <div class="brand-tile"><span class="brand-mark"></span><span class="brand-name">AUREL VANTA</span></div>
    <div class="brand-tile"><span class="brand-mark"></span><span class="brand-name">AUREL VANTA</span></div>
  </div>

  <div class="feature-row">
    <div class="feature-brand feature-brand--left"><span class="brand-mark"></span><span class="brand-name">AUREL VANTA</span></div>
    <div class="feature-brand feature-brand--center"><span class="brand-mark"></span><span class="brand-name">AUREL VANTA</span></div>
    <div class="feature-brand feature-brand--right"><span class="brand-mark"></span><span class="brand-name">AUREL VANTA</span></div>
  </div>

  <div class="tile-row" style="top:255px">
    <div class="brand-tile"><span class="brand-mark"></span><span class="brand-name">AUREL VANTA</span></div>
    <div class="brand-tile"><span class="brand-mark"></span><span class="brand-name">AUREL VANTA</span></div>
    <div class="brand-tile"><span class="brand-mark"></span><span class="brand-name">AUREL VANTA</span></div>
    <div class="brand-tile"><span class="brand-mark"></span><span class="brand-name">AUREL VANTA</span></div>
    <div class="brand-tile"><span class="brand-mark"></span><span class="brand-name">AUREL VANTA</span></div>
    <div class="brand-tile"><span class="brand-mark"></span><span class="brand-name">AUREL VANTA</span></div>
    <div class="brand-tile"><span class="brand-mark"></span><span class="brand-name">AUREL VANTA</span></div>
  </div>
  <div class="tile-row" style="top:303px">
    <div class="brand-tile"><span class="brand-mark"></span><span class="brand-name">AUREL VANTA</span></div>
    <div class="brand-tile"><span class="brand-mark"></span><span class="brand-name">AUREL VANTA</span></div>
    <div class="brand-tile"><span class="brand-mark"></span><span class="brand-name">AUREL VANTA</span></div>
    <div class="brand-tile"><span class="brand-mark"></span><span class="brand-name">AUREL VANTA</span></div>
    <div class="brand-tile"><span class="brand-mark"></span><span class="brand-name">AUREL VANTA</span></div>
    <div class="brand-tile"><span class="brand-mark"></span><span class="brand-name">AUREL VANTA</span></div>
  </div>
  <div class="tile-row" style="top:350px">
    <div class="brand-tile"><span class="brand-mark"></span><span class="brand-name">AUREL VANTA</span></div>
    <div class="brand-tile"><span class="brand-mark"></span><span class="brand-name">AUREL VANTA</span></div>
    <div class="brand-tile"><span class="brand-mark"></span><span class="brand-name">AUREL VANTA</span></div>
    <div class="brand-tile"><span class="brand-mark"></span><span class="brand-name">AUREL VANTA</span></div>
    <div class="brand-tile"><span class="brand-mark"></span><span class="brand-name">AUREL VANTA</span></div>
    <div class="brand-tile"><span class="brand-mark"></span><span class="brand-name">AUREL VANTA</span></div>
    <div class="brand-tile"><span class="brand-mark"></span><span class="brand-name">AUREL VANTA</span></div>
  </div>
  <div class="tile-row" style="top:398px">
    <div class="brand-tile"><span class="brand-mark"></span><span class="brand-name">AUREL VANTA</span></div>
    <div class="brand-tile"><span class="brand-mark"></span><span class="brand-name">AUREL VANTA</span></div>
    <div class="brand-tile"><span class="brand-mark"></span><span class="brand-name">AUREL VANTA</span></div>
    <div class="brand-tile"><span class="brand-mark"></span><span class="brand-name">AUREL VANTA</span></div>
    <div class="brand-tile"><span class="brand-mark"></span><span class="brand-name">AUREL VANTA</span></div>
    <div class="brand-tile"><span class="brand-mark"></span><span class="brand-name">AUREL VANTA</span></div>
  </div>
  <div class="tile-row" style="top:446px">
    <div class="brand-tile"><span class="brand-mark"></span><span class="brand-name">AUREL VANTA</span></div>
    <div class="brand-tile"><span class="brand-mark"></span><span class="brand-name">AUREL VANTA</span></div>
    <div class="brand-tile"><span class="brand-mark"></span><span class="brand-name">AUREL VANTA</span></div>
    <div class="brand-tile"><span class="brand-mark"></span><span class="brand-name">AUREL VANTA</span></div>
    <div class="brand-tile"><span class="brand-mark"></span><span class="brand-name">AUREL VANTA</span></div>
    <div class="brand-tile"><span class="brand-mark"></span><span class="brand-name">AUREL VANTA</span></div>
    <div class="brand-tile"><span class="brand-mark"></span><span class="brand-name">AUREL VANTA</span></div>
  </div>

  <div class="gold-rule"></div>
  <div class="skyline-band" role="img" aria-label="Gold line-art skyline of European landmarks, including a tower, bridges, domes and cathedrals, on a black band"></div>
</main>
</body>
</html>
```